THis will be a flyer to post around town for our Big Buck Contest. Here are the rules (which can be in small print). It should appeal to hunters. We are in Texas.

2014-2015 BIG BUCK CONTEST
OFFICIAL RULES:
1. Eligible hunters must be signed in and have $20 entry fee paid between November 1, 2014 - ____________________. Hunters may enter online @ www.brindlecreekhub.org or stop by The Pecan Hollow Area Chamber of Commerce for an entry form @ 418 E. Juniper Ave. on the square in Pecan Hollow.
2. Deer must be a whitetail buck killed during the general hunting season.
3. Bucks killed within a deer-proof fence or any other confined areas are not eligible to enter contest. Bucks that were EVER kept inside a pen for breeding purposes or any other reason are NOT allowed. Bucks that are tagged or tattooed are NOT allowed. Bucks cannot have been raised in a fenced in area and released. Bucks considered tame, domesticated or pet are NOT allowed.
4. Bucks must be properly tagged according to Texas State Law when brought in for measurement. Hunter must present valid hunting license and contest entry for to the official measurer.
5. Hunters attempting to cheat in the BIG BUCK CONTEST or violating Texas Game Laws are disqualified and barred from entering this contest for a period of time to be determined by the contest committee.
6. NO MORE than 1 prize will be awarded to any registered hunter. A hunter’s second buck is valid if it outscores first buck.
7. All entries must be brought in by the rightful. Any attempts to alter or enhance the horns in any from will be grounds for disqualification WITHOUT refund.
8. You must enter your buck in the contest within 72 hours of kill, unless prior arrangements have been made.

Measurements Guidelines:
For measurement, the hunter must bring the ENTIRE BODY of the field dressed animal to one of the official measurers.

Total $25.00
_____ Check ______ Money Order _____ Cashier Check
*** Please DO NOT DROP OFF OF MAIL CASH***

DROP OFF AT OR MAIL TO:

The Pecan Hollow Area Chamber of Commerce
418 E. Juniper Ave
Pecan Hollow, TX 76312

PRIZES:
1. Velmon Strouth Taxidermy - Shoulder Mount (donated)
>
> 2. 45 quart Kodo cooler sponsored by Ridgeway Timber and Fellowship of the Plains
>
> 3. 500 lbs of deer corn sponsored by Tanning Feed.

Target Market(s)

Texas deer hunters

Industry/Entity Type

Town

Requirements
Must have
• rules
• Fee amount $20
• Pecan Hollow Area Chamber of Commerce

```html
<!DOCTYPE html>
<html lang="en">
<head>
<meta charset="utf-8">
<title>2014-2015 Big Buck Contest</title>
<link rel="stylesheet" href="https://fonts.googleapis.com/css2?family=Roboto+Slab:wght@700;900&family=Arimo:wght@400;700&display=swap">
<style>
  :root {
    --bg-dark: #120d08;
    --bg-brown: #3a2a1a;
    --antler: #b59a72;
    --panel: #ffffff;
    --ink: #1a1a1a;
    --title: #ffffff;
    --accent: #c9a06a;
  }
  * { box-sizing: border-box; margin: 0; padding: 0; }
  html, body { width: 900px; height: 1200px; overflow: hidden; background: var(--bg-dark); }
  .flyer {
    position: relative; width: 900px; height: 1200px; overflow: hidden;
    font-family: "Arimo", Arial, sans-serif; color: var(--ink);
  }
  .backdrop {
    position: absolute; inset: 0;
    background:
      radial-gradient(ellipse 360px 300px at 690px 330px, #6b5238 0%, #3b2b1b 45%, transparent 75%),
      radial-gradient(ellipse 700px 500px at 600px 700px, var(--bg-brown) 0%, var(--bg-dark) 80%);
  }
  .headline { position: absolute; top: 14px; left: 0; width: 100%; text-align: center; color: var(--title);
    font-family: "Roboto Slab", Georgia, serif; text-shadow: 0 3px 6px rgba(0,0,0,.7); }
  .headline .season { font-size: 56px; font-weight: 700; line-height: 1; letter-spacing: 1px; }
  .headline .contest { font-size: 92px; font-weight: 900; line-height: 1.05; letter-spacing: 1px; }
  .rules-panel {
    position: absolute; left: 50px; top: 256px; width: 456px; height: 764px;
    background: var(--panel); padding: 16px 18px; font-size: 13.6px; line-height: 1.3;
  }
  .panel-title { font-weight: 700; font-size: 17px; margin-bottom: 8px; }
  .rules-list { list-style: none; }
  .rules-list li { margin-bottom: 12px; }
  .blank { display: inline-block; border-bottom: 1px solid var(--ink); width: 110px; }
  .measure-panel {
    position: absolute; left: 512px; top: 580px; width: 360px; height: 410px;
    background: var(--panel); padding: 14px 16px; font-size: 13px; line-height: 1.3;
  }
  .measure-panel p { margin-bottom: 10px; }
  .measure-panel .strong { font-weight: 700; }
  .short-blank { display: inline-block; border-bottom: 1px solid var(--ink); width: 36px; }
  .prizes ol { list-style: none; }
  .prizes li { margin-bottom: 8px; }
  .footer-name {
    position: absolute; left: 0; bottom: 40px; width: 100%; text-align: center;
    color: var(--title); font-family: "Roboto Slab", Georgia, serif; font-weight: 700;
    font-size: 44px; line-height: 1.1;
  }
</style>
</head>
<body>
<main class="flyer">
  <div class="backdrop" role="img" aria-label="Photograph of a large whitetail buck with wide antlers against a dark background"></div>

  <header class="headline">
    <div class="season">2014-2015</div>
    <div class="contest">BIG BUCK CONTEST</div>
  </header>

  <section class="rules-panel">
    <h2 class="panel-title">OFFICIAL RULES:</h2>
    <ol class="rules-list">
      <li>1. Eligible hunters must be signed in and have $20 entry fee paid between November 1, 2014 - <span class="blank"></span>. Hunters may enter online @ www.brindlecreekhub.org or stop by The Pecan Hollow Area Chamber of Commerce for an entry form @ 418 E. Juniper Ave. on the square in Pecan Hollow.</li>
      <li>2. Deer must be a whitetail buck killed during the general hunting season.</li>
      <li>3. Bucks killed within a deer-proof fence or any other confined areas are not eligible to enter contest. Bucks that were EVER kept inside a pen for breeding purposes or any other reason are NOT allowed. Bucks that are tagged or tattooed are NOT allowed. Bucks cannot have been raised in a fenced in area and released. Bucks considered tame, domesticated or pet are NOT allowed.</li>
      <li>4. Bucks must be properly tagged according to Texas State Law when brought in for measurement. Hunter must present valid hunting license and contest entry for to the official measurer.</li>
      <li>5. Hunters attempting to cheat in the BIG BUCK CONTEST or violating Texas Game Laws are disqualified and barred from entering this contest for a period of time to be determined by the contest committee.</li>
      <li>6. NO MORE than 1 prize will be awarded to any registered hunter. A hunter’s second buck is valid if it outscores first buck.</li>
      <li>7. All entries must be brought in by the rightful. Any attempts to alter or enhance the horns in any from will be grounds for disqualification WITHOUT refund.</li>
      <li>8. You must enter your buck in the contest within 72 hours of kill, unless prior arrangements have been made.</li>
    </ol>
  </section>

  <section class="measure-panel">
    <h2 class="panel-title">MEASUREMENTS GUIDELINES:</h2>
    <p>For measurement, the hunter must bring the ENTIRE BODY of the field dressed animal to one of the official measurers.</p>
    <p><span class="strong">Total $25.00</span><br>
      <span class="short-blank"></span> Check <span class="short-blank"></span> Money Order <span class="short-blank"></span> Cashier Check<br>
      *** Please DO NOT DROP OFF OF MAIL CASH***</p>
    <p class="strong">DROP OFF AT OR MAIL TO:</p>
    <p>The Pecan Hollow Area Chamber of Commerce<br>418 E. Juniper Ave<br>Pecan Hollow, TX 76312</p>
    <div class="prizes">
      <p class="strong">PRIZES:</p>
      <ol>
        <li>1. Velmon Strouth Taxidermy - Shoulder Mount (donated)</li>
        <li>2. 45 quart Kodo cooler sponsored by Ridgeway Timber and Fellowship of the Plains</li>
        <li>3. 500 lbs of deer corn sponsored by Tanning Feed.</li>
      </ol>
    </div>
  </section>

  <footer class="footer-name">Pecan Hollow Area Chamber of Commerce</footer>
</main>
</body>
</html>
```